Psychology Practice in Sydney Website Redesign

Corlew Psychology is a Psychology Practice with locations in Westmead, Chatswood and the CBD. They have specialties in treating children, and in treating eating disorders. They also treat anxiety and depression. They have ~10-20 clinical psychologists working for them.

The client wants the site to be modern and professional, he said:
”Mainly gonna be the credibility, people already know of us, but some could find us on google search, site needs to be a bit sexy.”

The client prefers websites with a heavy use of negative space and a largely minimal, modern design. (e.g. https://harbourlanemind-example.com.au/, https://www.fenmora-example.net.au/, https://tovalin-example.com.au/). He wants the site to be approachable without being unprofessional, and to be modern without being clinical. This is their current site: https://www.corlewpsychology-example.com.au/

The client wants the site to be a one pager design (like the sites given above). Please include a section named “Our Specialisations”, and the next titled “What we treat”, then one titled “Our Team” Feel free to take inspiration from the included links for the layout of these parts of the site.

Please mock up a booking panel similar to the that appears when you click "book now" on https://www.quillbrookcare-example.com.au/# .

The client would prefer you use the current logo and colour green (in logo) for theming.

Current site: https://www.corlewpsychology-example.com.au/

The winning designers will be required to:
- Provide a secondary standard page template
- Provide a design for a flyout enquiry/booking form
- Supply all images used in the designs free of charge

```html
<!DOCTYPE html>
<html lang="en">
<head>
<meta charset="utf-8">
<title>Corlew Psychology</title>
<link rel="stylesheet" href="https://fonts.googleapis.com/css2?family=Rajdhani:wght@500;600;700&family=Montserrat:wght@400;500;600;700&display=swap">
<style>
:root{
  --green:#5fbd7e;
  --green-soft:#7fcf97;
  --band:#d2fbe1;
  --footer:#6cc588;
  --ink:#2f2f2f;
  --muted:#555;
  --card:#e8e8e8;
  --dark:#2e2e2e;
  --white:#fff;
  --alert:#f0001d;
}
*{margin:0;padding:0;box-sizing:border-box}
html,body{width:1200px;height:4808px;overflow:hidden}
body{position:relative;background:var(--white);font-family:"Montserrat",sans-serif;color:var(--ink)}
.abs{position:absolute}
.heading{font-family:"Rajdhani",sans-serif;font-weight:600;letter-spacing:1px;text-transform:uppercase}
.rule{display:inline-block;width:62px;height:4px;background:currentColor;vertical-align:middle;margin:0 10px}
.center-title{position:absolute;left:0;width:1200px;text-align:center;font-size:40px;color:var(--ink)}
.btn-outline{position:absolute;display:flex;align-items:center;justify-content:center;border:2px solid var(--green);border-radius:30px;color:var(--green);font-weight:600;font-size:15px;background:transparent}

/* header */
.site-header{top:0;left:0;width:1200px;height:130px;background:var(--white)}
.brand{left:67px;top:42px;display:flex;align-items:center;gap:10px}
.brand-mark{width:22px;height:22px;background:var(--green)}
.brand-name{font-weight:700;font-size:28px;color:var(--green);letter-spacing:.5px}
.nav{right:64px;top:58px;display:flex;gap:32px;font-size:12px;color:#9a9a9a}
.nav .active{color:var(--green)}

/* hero */
.hero{top:130px;left:0;width:1200px;height:710px;background:linear-gradient(100deg,#e9eee5 0%,#cfd8c6 40%,#7c9a6e 75%,#b7c2a8 100%)}
.hero-panel{left:80px;top:274px;width:478px;height:400px;background:rgba(108,190,130,.88);border-radius:12px;text-align:center;color:var(--white);padding-top:76px}
.hero-panel h1{font-family:"Rajdhani",sans-serif;font-weight:500;font-size:39px;line-height:43px;letter-spacing:1px}
.hero-panel p{font-size:11.5px;line-height:24px;margin:24px auto 0;width:380px}
.hero-btn{display:inline-flex;align-items:center;justify-content:center;margin-top:18px;width:294px;height:60px;background:var(--white);border-radius:14px;color:var(--ink);font-family:"Rajdhani",sans-serif;font-weight:600;font-size:20px}

/* about */
.about-photo{left:228px;top:940px;width:310px;height:310px;border-radius:50%;border:8px solid var(--green);background:linear-gradient(135deg,#e7d8c8,#8a7a6a 55%,#2f3a3c);box-shadow:0 0 40px 14px rgba(95,189,126,.28)}
.about-title{left:605px;top:928px;font-size:40px;color:var(--green)}
.about-text{left:605px;top:996px;width:500px;font-size:15px;line-height:32px;color:#444}

/* clinics */
.clinic{width:330px;text-align:center}
.clinic-photo{width:134px;height:134px;border-radius:50%;margin:0 auto}
.clinic h3{font-weight:500;font-size:18px;margin-top:24px;color:var(--ink);letter-spacing:.5px}
.clinic p{font-size:11.5px;line-height:24px;color:#555;margin:18px auto 0;width:280px}
.clinic .more{display:block;margin-top:12px;font-size:15px;font-weight:600;color:#444}
.dots{top:1850px;left:580px;display:flex;gap:14px}
.dots span{width:14px;height:14px;border-radius:50%;background:var(--white)}
.dots span+span{background:#777}

/* what we do */
.treat-title{color:var(--green)}
.treat-card{top:2118px;width:334px;height:348px;background:var(--card);border-radius:16px;text-align:center;padding:14px 14px 0}
.treat-card.featured{background:var(--white);border:3px solid #bfe8cc}
.treat-photo{height:144px;border-radius:10px}
.treat-card h3{font-family:"Rajdhani",sans-serif;font-weight:600;font-size:22px;color:var(--green);margin-top:22px;letter-spacing:.5px}
.treat-card p{font-size:11px;line-height:20px;color:#555;margin:10px auto 0;width:285px}
.treat-card .btn-outline{left:50%;transform:translateX(-50%);bottom:22px;width:152px;height:40px;font-size:11px}

/* team */
.team-card{top:2812px;width:276px;height:245px;border-radius:10px;overflow:hidden;box-shadow:0 3px 8px rgba(0,0,0,.15)}
.team-photo{height:181px}
.team-bar{height:64px;background:var(--dark);color:var(--green-soft);display:flex;align-items:center;justify-content:center;gap:6px;font-weight:700;font-size:15px}
.btn-grey{position:absolute;left:521px;top:3099px;width:158px;height:50px;border:2px solid #555;border-radius:14px;background:#9b9b9b;color:#333;display:flex;align-items:center;justify-content:center;font-weight:600;font-size:16px}

/* resources */
.res-photo{left:380px;top:3219px;width:820px;height:660px;background:linear-gradient(90deg,#fff 0%,rgba(255,255,255,0) 35%),linear-gradient(160deg,#e4eaee,#b9c6cc 45%,#6a7784 75%,#c9a69c)}
.res-title{left:66px;top:3316px;font-size:44px;color:var(--green)}
.res-intro{left:66px;top:3378px;width:480px;font-size:15px;line-height:24px;color:var(--green)}
.res-list{left:92px;top:3440px;list-style:none;font-size:15px;color:var(--green)}
.res-list li{height:32px}
.res-list li::before{content:"";display:inline-block;width:6px;height:6px;border-radius:50%;background:var(--ink);margin-right:8px;vertical-align:middle;margin-left:-14px}

/* contact */
.contact-photo{left:146px;top:4014px;width:425px;height:371px;border:2px solid #555;background:linear-gradient(135deg,#e6e2dc,#b9cad3 45%,#7c9fb2 70%,#f1efec)}
.field{position:absolute;border:2px solid #555;font-size:12px;color:#888;padding:26px 0 0 12px}
.send{left:605px;top:4322px;width:120px;height:62px;border-radius:18px;background:#555;color:var(--white);font-family:"Rajdhani",sans-serif;font-weight:700;font-size:22px;display:flex;align-items:center;justify-content:center}

/* footer */
.footer{left:0;top:4400px;width:1200px;height:408px}
.foot-h{font-weight:600;font-size:19px;color:var(--white)}
.foot-links{list-style:none;font-size:11px;color:var(--white);line-height:24px}
.foot-links li::before{content:"› "}
.foot-contact{font-size:13px;color:var(--white);line-height:22px}
.news-input{width:156px;height:38px;background:var(--white);border:1px solid #ddd;font-size:10px;color:#aaa;padding:12px 0 0 12px}
.subscribe{width:136px;height:44px;border-radius:22px;background:var(--alert);color:var(--white);font-size:13px;font-weight:700;display:flex;align-items:center;justify-content:center}
.copyright{top:4770px;left:0;width:1200px;text-align:center;font-size:14px;color:var(--white)}
</style>
</head>
<body>

<header class="site-header abs">
  <div class="brand abs"><span class="brand-mark"></span><span class="brand-name">Corlew Psychology</span></div>
  <nav class="nav abs">
    <span class="active">Home</span><span>About Us</span><span>Our Specialisations</span><span>What we treat</span><span>Our Team</span><span>Resources</span><span>Contact Us</span>
  </nav>
</header>

<section class="hero abs" role="img" aria-label="Photo of a smiling woman hugging a person in a green sweater"></section>
<svg class="abs" style="left:0;top:770px" width="1200" height="80" viewBox="0 0 1200 80" preserveAspectRatio="none"><path d="M0 60 C250 10 420 80 700 40 C900 10 1050 20 1200 30 L1200 80 L0 80Z" fill="#fff"/></svg>
<div class="hero-panel abs">
  <h1>RESOURCES FOR HEALTH<br>CARE PROFESSIONALS</h1>
  <p>You may be surprised to learn how common psychological problems are, and how commonly our emotions stop us from achieving the happiness that we could otherwise attain.</p>
  <span class="hero-btn">BOOK AN APPOINTMENT</span>
</div>

<section class="about">
  <div class="about-photo abs" role="img" aria-label="Photo of a client talking with a psychologist on a sofa"></div>
  <h2 class="about-title abs heading">About Us<span class="rule" style="width:64px"></span></h2>
  <p class="about-text abs">we are all clinical psychologists with post-graduate clinical<br>training. We have enough specialists in different conditions, so<br>you will find the right psychologist to work with you.<br>Our clinicians are committed to &nbsp;staying up to date with<br>research into the causes and treatments of common<br>conditions.</p>
  <span class="btn-outline" style="left:605px;top:1205px;width:156px;height:51px">Read More</span>
</section>

<svg class="abs" style="left:0;top:1330px" width="1200" height="630" viewBox="0 0 1200 630" preserveAspectRatio="none"><path d="M0 30 C300 -5 500 45 800 25 C1000 10 1120 10 1200 20 L1200 560 C1000 600 800 580 600 600 C350 625 150 600 0 610Z" fill="#d2fbe1"/></svg>
<section class="clinics">
  <h2 class="center-title heading" style="top:1390px"><span class="rule"></span>Our Specialist Clinics<span class="rule"></span></h2>
  <div class="clinic abs" style="left:72px;top:1485px">
    <div class="clinic-photo" role="img" aria-label="Photo of a person wearing a virtual reality headset" style="background:linear-gradient(135deg,#dfe7f2,#6b87b5)"></div>
    <h3>VIRTUAL REALITY CLINIC</h3>
    <p>We have the combined software and hardware to provide VR-based treatments of phobias, especially for fears of flying, driving in tunnels, heights, closed spaces, public speaking, dogs and several other situations.</p>
    <span class="more">Read More..</span>
  </div>
  <div class="clinic abs" style="left:438px;top:1485px">
    <div class="clinic-photo" role="img" aria-label="Photo of a woman looking at a plate of food" style="background:linear-gradient(135deg,#c98a5c,#3b2a20)"></div>
    <h3>EATING DISORDERS</h3>
    <p>We provide assessment and treatment of all eating disorders, including anorexia nervosa, bulimia nervosa, binge eating, picky and avoidant eating (ARFID), and nocturnal eating syndrome. Our clinicians undergo</p>
    <span class="more">Read More..</span>
  </div>
  <div class="clinic abs" style="left:807px;top:1485px">
    <div class="clinic-photo" role="img" aria-label="Photo of a group of people standing in a bright hall" style="background:linear-gradient(135deg,#f2f2f2,#4a4f58)"></div>
    <h3>FND AND SOMATISATION</h3>
    <p>Functional Neurological Disorder (FND) is another term for conversion disorder, which is when a person's central nervous system is generating symptoms even though the body is fine and healthy. We have several</p>
    <span class="more">Read More..</span>
  </div>
  <div class="dots abs"><span></span><span></span></div>
</section>

<section class="what-we-do">
  <h2 class="center-title heading treat-title" style="top:2022px"><span class="rule"></span>What We Do<span class="rule"></span></h2>
  <div class="treat-card abs" style="left:88px">
    <div class="treat-photo" role="img" aria-label="Photo of a worried man holding his head" style="background:linear-gradient(135deg,#dfe6ea,#5a7896)"></div>
    <h3>DEPRESSION &amp; ANXIETY</h3>
    <p>For when you feel sad, worried, overwhelmed, low, disconnected, or like the world is closing in on you.</p>
    <span class="btn-outline">Find Out More</span>
  </div>
  <div class="treat-card featured abs" style="left:435px">
    <div class="treat-photo" role="img" aria-label="Photo of a child in front of a chalkboard full of formulas" style="background:linear-gradient(135deg,#3a4542,#1f2624)"></div>
    <h3>ADHD &amp; NEURODIVERSITY</h3>
    <p>For when you need a helping hand with the challenges that neurodiversity brings and the unique experiences that come with it.</p>
    <span class="btn-outline">Find Out More</span>
  </div>
  <div class="treat-card abs" style="left:786px">
    <div class="treat-photo" role="img" aria-label="Photo of a family sitting together on grass" style="background:linear-gradient(135deg,#c9a27a,#5f7a3e)"></div>
    <h3>CHILD &amp; FAMILY</h3>
    <p>For when you feel sad, worried, overwhelmed, low, disconnected, or like the world is closing in on you.</p>
    <span class="btn-outline">Find Out More</span>
  </div>
  <span class="btn-outline" style="left:522px;top:2528px;width:159px;height:49px;font-size:16px">View More</span>
</section>

<svg class="abs" style="left:0;top:2590px" width="1200" height="640" viewBox="0 0 1200 640" preserveAspectRatio="none"><path d="M0 25 C300 0 600 40 900 20 C1050 10 1150 15 1200 10 L1200 600 C1000 630 800 600 600 610 C350 625 150 600 0 615Z" fill="#d2fbe1"/></svg>
<section class="team">
  <h2 class="center-title heading" style="top:2703px"><span class="rule"></span>Our Team<span class="rule"></span></h2>
  <div class="team-card abs" style="left:159px"><div class="team-photo" role="img" aria-label="Portrait of a smiling female doctor" style="background:linear-gradient(160deg,#eef1f2,#c9d3d6)"></div><div class="team-bar">VIEW MORE DETAILS <span>→</span></div></div>
  <div class="team-card abs" style="left:465px"><div class="team-photo" role="img" aria-label="Portrait of a smiling male doctor in scrubs" style="background:linear-gradient(160deg,#8a7c6c,#3f5d86)"></div><div class="team-bar">VIEW MORE DETAILS <span>→</span></div></div>
  <div class="team-card abs" style="left:773px"><div class="team-photo" role="img" aria-label="Portrait of a smiling doctor with a stethoscope" style="background:linear-gradient(160deg,#f4f4f2,#c9d6c2)"></div><div class="team-bar">VIEW MORE DETAILS <span>→</span></div></div>
  <span class="btn-grey">View More</span>
</section>

<section class="resources">
  <div class="res-photo abs" role="img" aria-label="Photo of smiling colleagues working at a laptop"></div>
  <h2 class="res-title abs heading">Resources<span class="rule"></span></h2>
  <p class="res-intro abs">We provide reliable and useful information about common emotional and behavioural problems.</p>
  <ul class="res-list abs">
    <li>Depression</li><li>Anxiety Disorders</li><li>Panic Attacks</li><li>Trauma and PTSD</li><li>Stress tips</li><li>Sleep Guide</li><li>Coping with grief</li><li>What is CBT?</li><li>Alcohol: How much is too much?</li><li>Quit smoking strategies</li>
  </ul>
  <span class="btn-outline" style="left:66px;top:3773px;width:158px;height:50px;background:#fff">Read More</span>
</section>

<svg class="abs" style="left:0;top:3840px" width="1200" height="590" viewBox="0 0 1200 590" preserveAspectRatio="none"><path d="M0 30 C300 0 500 10 700 20 C900 30 1050 0 1200 10 L1200 590 L0 590Z" fill="#d2fbe1"/></svg>
<section class="contact">
  <h2 class="center-title heading" style="top:3925px"><span class="rule"></span>Get In Touch<span class="rule"></span></h2>
  <div class="contact-photo abs" role="img" aria-label="Photo of masked medical staff working at a laptop"></div>
  <div class="field" style="left:605px;top:4014px;width:256px;height:60px">First Name *</div>
  <div class="field" style="left:871px;top:4014px;width:257px;height:60px">Last Name *</div>
  <div class="field" style="left:605px;top:4088px;width:256px;height:58px">Email *</div>
  <div class="field" style="left:871px;top:4088px;width:257px;height:58px">Phone Number *</div>
  <div class="field" style="left:605px;top:4161px;width:523px;height:144px">Message *</div>
  <span class="send abs">SEND</span>
</section>

<footer>
  <svg class="footer abs" viewBox="0 0 1200 408" preserveAspectRatio="none"><path d="M0 20 C250 45 500 50 700 35 C900 20 1050 0 1200 10 L1200 408 L0 408Z" fill="#6cc588"/></svg>
  <h4 class="foot-h abs" style="left:215px;top:4552px">Quick Links</h4>
  <ul class="foot-links abs" style="left:215px;top:4590px"><li>About Us</li><li>Our Specialisations</li><li>What we treat</li><li>Our Team</li><li>Resources</li></ul>
  <h4 class="foot-h abs" style="left:405px;top:4552px">Contact</h4>
  <div class="foot-contact abs" style="left:405px;top:4592px;display:flex;gap:12px">
    <svg width="14" height="14" viewBox="0 0 24 24" style="margin-top:4px"><path d="M6.6 10.8a15 15 0 0 0 6.6 6.6l2.2-2.2a1 1 0 0 1 1-.25 11 11 0 0 0 3.6.6 1 1 0 0 1 1 1V20a1 1 0 0 1-1 1A17 17 0 0 1 3 4a1 1 0 0 1 1-1h3.5a1 1 0 0 1 1 1c0 1.25.2 2.45.6 3.6a1 1 0 0 1-.25 1z" fill="#fff"/></svg>
    <span>0912 345 678</span>
  </div>
  <div class="foot-contact abs" style="left:405px;top:4640px;display:flex;gap:12px">
    <svg width="14" height="16" viewBox="0 0 24 24" style="margin-top:3px"><path d="M12 2a7 7 0 0 0-7 7c0 5 7 13 7 13s7-8 7-13a7 7 0 0 0-7-7zm0 9.5A2.5 2.5 0 1 1 12 6.5a2.5 2.5 0 0 1 0 5z" fill="#fff"/></svg>
    <span>14 Wrenfield Lane, Marlow Park,<br>Sydney-2150</span>
  </div>
  <h4 class="foot-h abs" style="left:756px;top:4552px">Newsletters</h4>
  <div class="news-input abs" style="left:756px;top:4592px">Enter your email</div>
  <span class="subscribe abs" style="left:756px;top:4644px">Subscribe</span>
  <p class="copyright abs">Copyright © 2013 – 2024 Corlew Psychology. All Rights Reserved.</p>
</footer>

</body>
</html>
```